Walk The Summit Book Cover Design

Book Cover Design Brief
Book Title
Walk The Summit
Subtitle
The 10 Quiet Habits of Remarkable Stewardship
Author
Doran Melisk
Overview
This book is about leadership that starts within.
Most leadership books focus on tactics or management strategies. This book focuses on the inner disciplines that create powerful leaders — mindset, integrity, focus, empathy, professionalism, honesty, and self-respect.
The tone of the book is bold, direct, confident, and transformational.
This is not a soft or corporate leadership book. It is a call to step up and become the leader you are capable of becoming.
The cover should feel:
• Powerful
• Professional
• Transformational
• Premium
• Memorable
Think best-selling leadership book, not a generic business book.
Target Audience
Business owners
Managers
Entrepreneurs
Team leaders
Professionals who want to grow as leaders
Most readers are ambitious professionals who want to level up their leadership and life.
Design Direction
The design should communicate:
Strength. Discipline. Leadership. Personal transformation.
Avoid cliché leadership visuals like:
• Handshakes
• Office buildings
• Corporate stock imagery
• Teams sitting around tables
The design should feel iconic, bold, and timeless.
Think about covers of successful leadership books such as:
Copper Rituals
Total Custody
Won't Bend Now
Begin From Where
The 52 Rules of Sway
These covers are simple, powerful, and recognizable even at small sizes.
Typography
The title WALK THE SUMMIT should be:
• Bold
• Strong
• Dominant on the cover
• Easy to read even at small sizes (important for Bravolo thumbnails)
The subtitle should be clean and secondary to the title.
The overall typography should feel strong, modern, and premium.
Color Direction
Designers are free to explore colors, but the cover should feel strong and premium, not playful.
Colors that often work well for leadership books include:
Black
Gold
White
Deep blue
Dark red
High contrast and clarity are important.
Style
Preferred style:
• Clean
• Modern
• Minimal
• Strong contrast
Avoid clutter and overly busy designs.
The goal is to create a cover that feels powerful and professional at first glance.
Deliverables
Front cover design for a leadership book.
Final files should include:
• High resolution artwork
• Editable source files
• Print-ready version suitable for publishing
Goal of the Cover
When someone sees this book on Bravolo or in a bookstore, they should immediately think:
“This looks like a serious leadership book.”
The design should feel like it belongs next to books by authors such as:
Marcus Threlby
Brasko Tandrel
Owen Marsh
Peter Halvorn
A strong, confident cover that attracts leaders who want to grow and perform at a higher level.
Updates
Target Market(s)
Business Owners and High level managers
Look and feel
Each slider illustrates characteristics of the customer's brand and the style your logo design should communicate.

```html
<!DOCTYPE html>
<html lang="en">
<head>
<meta charset="utf-8">
<title>Walk The Summit — Front Cover</title>
<link rel="stylesheet" href="https://fonts.googleapis.com/css2?family=Anton&family=Archivo+Black&family=Oswald:wght@500;600&display=swap">
<style>
  :root {
    --stage: #e8e8e6;
    --navy: #0a0633;
    --navy-deep: #05031f;
    --title-light: #ffffff;
    --title-shade: #d9d9dc;
    --collar: #e4e4e6;
    --tie-red: #b30d0d;
    --tie-dark: #7d0606;
    --text-light: #f2f2f4;
  }
  * { margin: 0; padding: 0; box-sizing: border-box; }
  html, body {
    width: 1200px;
    height: 800px;
    overflow: hidden;
    background: var(--stage);
  }
  .stage {
    position: relative;
    width: 1200px;
    height: 800px;
  }
  .cover {
    position: absolute;
    left: 355px;
    top: 30px;
    width: 490px;
    height: 740px;
    background: linear-gradient(90deg, var(--navy) 0%, var(--navy-deep) 100%);
  }
  .cover-art {
    display: block;
    width: 490px;
    height: 740px;
  }
  .title-main {
    font-family: "Anton", "Impact", sans-serif;
    font-size: 222px;
  }
  .title-lead {
    font-family: "Archivo Black", "Arial Black", sans-serif;
    font-size: 26px;
    fill: var(--navy);
  }
  .subtitle {
    font-family: "Oswald", "Arial Narrow", sans-serif;
    font-weight: 500;
    font-size: 19px;
    fill: var(--text-light);
  }
  .author {
    font-family: "Oswald", "Arial Narrow", sans-serif;
    font-weight: 600;
    font-size: 46px;
    fill: var(--text-light);
  }
</style>
</head>
<body>
<main class="stage">
  <section class="cover" aria-label="Walk The Summit front cover">
    <svg class="cover-art" viewBox="0 0 490 740" xmlns="http://www.w3.org/2000/svg">
      <defs>
        <linearGradient id="title-fill" x1="0" y1="0" x2="1" y2="0">
          <stop offset="0" stop-color="var(--title-light)"/>
          <stop offset="1" stop-color="var(--title-shade)"/>
        </linearGradient>
        <linearGradient id="collar-tie-fill" x1="0" y1="0" x2="0" y2="1">
          <stop offset="0" stop-color="var(--collar)"/>
          <stop offset="0.4" stop-color="var(--collar)"/>
          <stop offset="0.55" stop-color="var(--tie-red)"/>
          <stop offset="1" stop-color="var(--tie-dark)"/>
        </linearGradient>
      </defs>

      <rect class="collar-tie" x="200" y="38" width="165" height="500" rx="6"
            fill="url(#collar-tie-fill)"
            role="img" aria-label="Illustration of a white shirt collar with a red necktie"/>

      <text class="title-main" fill="url(#title-fill)"
            transform="translate(188 700) rotate(-90)"
            textLength="662" lengthAdjust="spacingAndGlyphs">SUMMIT</text>

      <rect class="title-lead-band" x="26" y="96" width="128" height="40" fill="var(--title-light)"/>
      <text class="title-lead" x="32" y="127" textLength="116" lengthAdjust="spacingAndGlyphs">WALK THE</text>

      <text class="subtitle" x="214" y="585" textLength="218" lengthAdjust="spacingAndGlyphs">THE 10 QUIET HABITS OF</text>
      <text class="subtitle" x="214" y="610" textLength="238" lengthAdjust="spacingAndGlyphs">REMARKABLE STEWARDSHIP</text>

      <text class="author" x="222" y="680" textLength="228" lengthAdjust="spacingAndGlyphs">DORAN MELISK</text>
    </svg>
  </section>
</main>
</body>
</html>
```